RAmio Shop Business Card Design

My auto shop is targeted to the European and Asian luxury automotive market. We do mechanics collision and parts.
Some of the makes are KTR, DQ, Stone Herald, Valdine,Norvi, solavanta, bremo, HJ, etc. But in the end we get all makes.
I don't want to have the makes logos on the business card.
The Name of the business is after my first Name Ramiro but without the s Ramio Shop if there is any other ideas about the name iam open to suggestions. And i don't have a LOGO. Need logo!
Updates

Reason: I increased my budget and invited more designers. And committed payment so giving you guys more time.

Target Market(s)

target is the luxury auto market

Industry/Entity Type

Automotive

Contact Information for Business Card

European Automotive Repair Shop, Collision Mechanics Parts
Ramiro Villalba Owner, Colibrí #14 Loma Serena 2

Requirements
Nice to have
• One design i can of liked was the use of the dash error logos like check engine light airbag light. Nobla press has this but dose not include the air bag light. For the collision part of the business. But am open to any design.
Should not have
• exact logo makes on front of card.

```html
<!DOCTYPE html>
<html lang="en">
<head>
<meta charset="utf-8">
<title>Ramiro Cars Business Card</title>
<link rel="stylesheet" href="https://fonts.googleapis.com/css2?family=Tinos&display=swap">
<style>
  :root {
    --backdrop: #e6e2dd;
    --card: #302e30;
    --ink: #f4f2f0;
    --ink-soft: #d9d6d3;
    --shadow: rgba(40, 30, 25, 0.28);
  }
  * { margin: 0; padding: 0; box-sizing: border-box; }
  html, body {
    width: 1200px;
    height: 900px;
    overflow: hidden;
    background: var(--backdrop);
  }
  .canvas {
    position: relative;
    width: 1200px;
    height: 900px;
  }
  .card {
    position: absolute;
    left: 320px;
    width: 560px;
    height: 320px;
    background: var(--card);
    box-shadow: 0 14px 30px var(--shadow);
    font-family: "Tinos", "Times New Roman", serif;
    color: var(--ink);
  }
  .card--front { top: 100px; }
  .card--back { top: 480px; }

  .brand {
    position: absolute;
    left: 0;
    right: 0;
    top: 50%;
    transform: translateY(-50%);
    display: flex;
    align-items: center;
    justify-content: center;
    gap: 22px;
  }
  .brand-mark {
    width: 44px;
    height: 44px;
    border-radius: 50%;
    background: var(--ink);
    flex: none;
  }
  .brand-name {
    font-size: 60px;
    font-weight: 400;
    line-height: 1;
    letter-spacing: 1px;
    color: var(--ink);
  }

  .details {
    position: absolute;
    left: 44px;
    top: 40px;
    list-style: none;
    font-size: 23px;
    line-height: 1.3;
    color: var(--ink-soft);
  }
  .address {
    position: absolute;
    left: 44px;
    bottom: 44px;
    font-size: 21px;
    font-style: normal;
    color: var(--ink-soft);
    letter-spacing: 1px;
  }
</style>
</head>
<body>
<main class="canvas">
  <section class="card card--front" aria-label="Business card front">
    <div class="brand">
      <span class="brand-mark" aria-hidden="true"></span>
      <p class="brand-name">Ramiro Cars</p>
    </div>
  </section>

  <section class="card card--back" aria-label="Business card back">
    <ul class="details">
      <li>European Automotive Repair Shop</li>
      <li>Collision Mechanics Parts</li>
      <li>Ramiro Villalba Owner</li>
    </ul>
    <address class="address">Colibrí #14 Loma Serena 2</address>
  </section>
</main>
</body>
</html>
```